Exciting Poster Project: 4 posters for Employee Benefit Program

We are an entrepreneurial healthcare IT company that is creating an internal campaign to launch our 2017 Culture and Professional Development goals for our internal staff.

We need 4 posters utilizing the 4 campaign logos (attached) that are tied together visually into a cohesive campaign.

A PPT is included that shows the other wall art that currently exists on the walls. The new posters will share a space with these pieces.

The posters may be mounted side by side, or stand alone on a wall- so the design should work both ways. Each poster should include its own icon and the tag line provided along with topics provided that fall under this category. The posters size can be dictated by your design, but the text should be legible from a minimum of 8 feet away.

At the bottom of each poster should include all 4 icons in order to tie the entire campaign together (perhaps they can be arranged together like a diamond shape with the primary one as the biggest diamond)

Our company website for our external branding is: www.pelmaroq.com
We have included our branding guidelines for our external brand, and ppts and graphics for our internal brand.

1) Poster 1:
a. Header: Better Today Than Yesterday
b. Sub-title: Personal and Professional Growth
c. Description: We are committed to helping you build on your strengths and passions and support you your career advancement goals. We have a variety of training and development programs available to help you reach your top potential!
Leadership Development Programs
1. Supervisor Training
2. Women’s Leadership
3. Leadership Meet-Ups
4. MBA Program
Staff Development
1. Continuing Education Fund
2. Book Club
3. Pelmaroq University
4. Mentorship
5. Learning Libraries
6. Department Wide Training Events

2) Poster 2:
a. Header: Perform at Highest Capacity
b. Sub-title: Be Your Best Self
c. Description: We are committed to providing programs that bring focus to your health and overall personal wellness to encourage a well balanced life
i. Healthy Living
1. Health and wellness seminars
2. Nutrition: Fruit Delivery
ii. Fitness:
1. Step Challenge
2. Virtual 5k
3. Recess
4. Golf Lessons
5. Ping Pong Club
iii. Creativity:
1. Painting
2. Photography Club
3. Virtual Trivia
iv. Mental Health:
1. Massage Therapy
2. EAP Education
v. Financial
1. 401(k)
2. Retirement education/financial planning seminars
3. Global Insurance Program education

3) Poster 3:
a. Header: Passionate Urgent and Driven to Success
b. Sub-Header: Innovation and Strategy
c. Description: We are committed to helping you connect the dots both in the industry and with our internal goals , mission, and vision.
i. Quarterly All-Hands
ii. Lumiverse
1. Internally: Departmental and Product Updates
2. Externally: Industry Knowledge
3. Culturally: Peer to Peer Community

4) Poster 4:
a. Header: Succeed as a Team
b. Sub-Header: Cultivating Collaboration
c. Description: We are committed to creating a culture of appreciation, teamwork, and supporting an open communication. All feedback and ideas are welcome here!
i. Team Building Events
1. Employee Focused
a. Summer Picnic
b. Employee Appreciation
c. Diwali
d. Holiday Party
e. Department Appreciation
2. Family Friendly
a. Halloween
b. Bring your Kids to Work Day
3. Awards
a. Peer to Peer: QuickNod Awards
b. Leadership: Crest of Merit
4. Surveys
a. New Hire
b. Employee Engagement
Updates

Target Market(s)

Internal Employees

Industry/Entity Type

Healthcare

Font styles to use
Sans Serif

Requirements
Must have
• Job Type: Posters
• Task Outline: Create Vector Art for 4 icons and 4 posters
• Fonts and Styles to Use: SourceSansPro
Nice to have
• There is an attachment with suggested concepts and styles that we like.
Should not have
• The poster should not be very wordy or hard to read in passing.

```html
<!DOCTYPE html>
<html lang="en">
<head>
<meta charset="utf-8">
<title>Pelmaroq Culture Campaign Posters</title>
<link href="https://fonts.googleapis.com/css2?family=Source+Sans+3:wght@400;600;700;900&display=swap" rel="stylesheet">
<style>
:root{
  --green:#8cc63f; --green-dark:#5f9a2a;
  --purple:#5b2a86; --purple-dark:#3f1a63;
  --teal:#1ba0b5; --teal-dark:#0f6f86;
  --orange:#f7941d; --orange-dark:#d8701a;
  --navy:#1f3f73; --brand:#1f5fa8;
  --ink:#4a4a4a; --rule:#d9d9d9; --page:#ffffff;
}
*{box-sizing:border-box;margin:0;padding:0}
html,body{width:870px;height:1200px;overflow:hidden;background:var(--page);font-family:"Source Sans 3",Arial,sans-serif;color:var(--ink)}
.campaign{position:relative;width:870px;height:1200px;display:grid;grid-template-columns:420px 420px;grid-template-rows:585px 585px;gap:10px 10px;padding:10px 10px}
.poster{position:relative;background:#fff;box-shadow:0 0 0 1px #e3e3e3;display:flex;flex-direction:column;overflow:hidden}
.poster__header{position:relative;height:205px;overflow:hidden}
.poster__header svg{position:absolute;inset:0;width:100%;height:100%}
.headline{position:absolute;font-weight:900;text-transform:uppercase;line-height:.9;color:#fff}
.poster__body{padding:12px 22px 0;flex:1}
.topic{display:flex;align-items:center;gap:12px;margin-bottom:8px}
.topic__icon{width:40px;height:40px;border-radius:50%;flex:none}
.topic__title{font-size:20px;font-weight:700}
.intro{font-size:10px;line-height:1.35;margin-bottom:10px}
.boxes{display:grid;gap:8px}
.box{border:1px solid var(--rule)}
.box__head{color:#fff;font-weight:700;font-size:9px;text-transform:uppercase;padding:4px 7px;line-height:1.15}
.box ul{list-style:none;padding:5px 8px 6px;font-size:9px;line-height:1.35}
.box li::before{content:"• "}
.poster__footer{height:62px;border-top:1px solid var(--rule);margin:0 22px;display:flex;align-items:center;justify-content:space-between}
.icon-set{width:70px;height:40px;border-radius:4px}
.icon-set--growth{background:linear-gradient(90deg,var(--green),#b7dc84)}
.icon-set--wellness{background:linear-gradient(90deg,var(--purple),#9b78bb)}
.icon-set--innovation{background:linear-gradient(90deg,var(--teal),#7fcbd7)}
.icon-set--collaboration{background:linear-gradient(90deg,var(--orange),#fbc27e)}
.brand{display:flex;align-items:center;gap:6px;font-weight:900;font-size:22px;color:var(--brand)}
.brand__mark{width:10px;height:10px;background:var(--brand)}
.bullets{list-style:none;font-size:10px;font-weight:700;line-height:1.5;margin-bottom:8px}
.bullets li::before{content:"■ ";color:var(--teal)}
</style>
</head>
<body>
<main class="campaign">

<section class="poster poster--growth">
  <div class="poster__header">
    <svg viewBox="0 0 420 205" preserveAspectRatio="none" aria-hidden="true">
      <rect width="420" height="205" fill="#8cc63f"/>
      <polygon points="0,0 150,0 0,150" fill="#9fd053"/>
      <polygon points="420,0 420,205 250,205" fill="#7ab634"/>
      <polygon points="300,0 420,0 420,120" fill="#a8d862"/>
      <polygon points="150,205 260,90 370,205" fill="#6fa82d"/>
    </svg>
    <div class="headline" style="left:22px;top:32px">
      <div style="font-size:56px">Better</div>
      <div style="font-size:56px;color:var(--navy)">Today</div>
      <div style="font-size:22px;letter-spacing:1px;margin-top:4px">Than Yesterday</div>
    </div>
  </div>
  <div class="poster__body">
    <div class="topic"><div class="topic__icon" style="background:var(--green)" role="img" aria-label="Growth category icon"></div><div class="topic__title" style="color:var(--green-dark)">Personal and Professional Growth</div></div>
    <p class="intro">We are committed to helping you build on your strengths and passions and support your career advancement goals. We have a variety of training and development programs available to help you reach your top potential!</p>
    <div class="boxes" style="grid-template-columns:1fr 1fr">
      <div class="box"><div class="box__head" style="background:var(--green)">Leadership Development Programs</div>
        <ul><li>Supervisor Training</li><li>Women's Leadership</li><li>Leadership Meet-Ups</li><li>MBA Program</li></ul></div>
      <div class="box"><div class="box__head" style="background:var(--green)">Staff Development</div>
        <ul><li>Continuing Education Fund</li><li>Book Club</li><li>Pelmaroq University</li><li>Mentorship</li><li>Learning Libraries</li><li>Department Wide Training Events</li></ul></div>
    </div>
  </div>
  <div class="poster__footer">
    <div class="icon-set icon-set--growth" role="img" aria-label="Campaign icon set, growth icon leading"></div>
    <div class="brand"><span class="brand__mark"></span>Pelmaroq</div>
  </div>
</section>

<section class="poster poster--wellness">
  <div class="poster__header">
    <svg viewBox="0 0 420 205" preserveAspectRatio="none" aria-hidden="true">
      <rect width="420" height="205" fill="#5b2a86"/>
      <polygon points="0,205 0,60 140,205" fill="#4a1f72"/>
      <polygon points="280,0 420,0 420,140" fill="#6c3a99"/>
      <polygon points="330,205 400,140 420,160 420,205" fill="#f7941d"/>
    </svg>
    <div class="headline" style="left:0;right:0;top:34px;text-align:center">
      <div style="font-size:30px;letter-spacing:1px">Perform At</div>
      <div style="font-size:60px;color:var(--orange)">Highest</div>
      <div style="font-size:40px">Capacity</div>
    </div>
  </div>
  <div class="poster__body">
    <div class="topic"><div class="topic__icon" style="background:var(--purple)" role="img" aria-label="Wellness category icon"></div><div class="topic__title" style="color:var(--purple)">Be Your Best Self</div></div>
    <p class="intro">We are committed to providing programs that bring focus to your health and overall personal wellness to encourage a well balanced life.</p>
    <div class="boxes" style="grid-template-columns:1fr 1fr 1fr">
      <div class="box"><div class="box__head" style="background:var(--orange)">Healthy Living</div><ul><li>Health and wellness seminars</li></ul></div>
      <div class="box"><div class="box__head" style="background:var(--orange)">Nutrition</div><ul><li>Fruit Delivery</li></ul></div>
      <div class="box"><div class="box__head" style="background:var(--orange)">Mental Health</div><ul><li>Massage Therapy</li><li>EAP Education</li></ul></div>
      <div class="box"><div class="box__head" style="background:var(--purple)">Financial</div><ul><li>401(k)</li><li>Retirement education / financial planning seminars</li><li>Global Insurance Program education</li></ul></div>
      <div class="box"><div class="box__head" style="background:var(--purple)">Fitness</div><ul><li>Step Challenge</li><li>Virtual 5k</li><li>Recess</li><li>Golf Lessons</li><li>Ping Pong Club</li></ul></div>
      <div class="box"><div class="box__head" style="background:var(--purple)">Creativity</div><ul><li>Painting</li><li>Photography Club</li><li>Virtual Trivia</li></ul></div>
    </div>
  </div>
  <div class="poster__footer">
    <div class="icon-set icon-set--wellness" role="img" aria-label="Campaign icon set, wellness icon leading"></div>
    <div class="brand"><span class="brand__mark"></span>Pelmaroq</div>
  </div>
</section>

<section class="poster poster--innovation">
  <div class="poster__header">
    <svg viewBox="0 0 420 205" preserveAspectRatio="none" aria-hidden="true">
      <rect width="420" height="205" fill="#1ba0b5"/>
      <polygon points="0,0 200,0 0,180" fill="#23b0c4"/>
      <polygon points="420,205 420,40 250,205" fill="#138aa0"/>
      <polygon points="330,0 420,0 420,80" fill="#8cc63f"/>
    </svg>
    <div class="headline" style="left:22px;top:30px">
      <div style="font-size:34px">Passionate</div>
      <div style="font-size:34px">Urgent <span style="font-size:22px">and</span></div>
      <div style="font-size:46px;color:var(--navy)">Driven to</div>
      <div style="font-size:46px">Success</div>
    </div>
  </div>
  <div class="poster__body">
    <div class="topic"><div class="topic__icon" style="background:var(--teal)" role="img" aria-label="Innovation category icon"></div><div class="topic__title" style="color:var(--teal-dark)">Innovation and Strategy</div></div>
    <p class="intro">We are committed to helping you connect the dots both in the industry and with our internal goals, mission, and vision.</p>
    <ul class="bullets"><li>QUARTERLY ALL-HANDS</li><li>LUMIVERSE</li></ul>
    <div class="boxes" style="grid-template-columns:1fr 1fr 1fr">
      <div class="box"><div class="box__head" style="background:var(--green)">Externally</div><ul><li>Industry Knowledge</li></ul></div>
      <div class="box"><div class="box__head" style="background:var(--teal)">Internally</div><ul><li>Departmental and Product Updates</li></ul></div>
      <div class="box"><div class="box__head" style="background:var(--navy)">Culturally</div><ul><li>Peer to Peer Community</li></ul></div>
    </div>
  </div>
  <div class="poster__footer">
    <div class="icon-set icon-set--innovation" role="img" aria-label="Campaign icon set, innovation icon leading"></div>
    <div class="brand"><span class="brand__mark"></span>Pelmaroq</div>
  </div>
</section>

<section class="poster poster--collaboration">
  <div class="poster__header">
    <svg viewBox="0 0 420 205" preserveAspectRatio="none" aria-hidden="true">
      <rect width="420" height="205" fill="#f7941d"/>
      <polygon points="0,0 120,0 0,120" fill="#f9a53c"/>
      <polygon points="420,205 420,60 280,205" fill="#e5801a"/>
      <polygon points="210,30 330,102 210,175 90,102" fill="#5b2a86"/>
    </svg>
    <div class="headline" style="left:0;right:0;top:66px;text-align:center">
      <div style="font-size:40px">Succeed As A</div>
      <div style="font-size:52px">Team</div>
    </div>
  </div>
  <div class="poster__body">
    <div class="topic"><div class="topic__icon" style="background:var(--orange)" role="img" aria-label="Collaboration category icon"></div><div class="topic__title" style="color:var(--orange-dark)">Cultivating Collaboration</div></div>
    <p class="intro">We are committed to creating a culture of appreciation, teamwork, and supporting an open communication. All feedback and ideas are welcome here!</p>
    <div class="boxes" style="grid-template-columns:1fr 1fr">
      <div class="box"><div class="box__head" style="background:var(--orange)">Awards</div><ul><li>Peer to Peer: QuickNod Awards</li><li>Leadership: Crest of Merit</li></ul></div>
      <div class="box"><div class="box__head" style="background:var(--orange)">Surveys</div><ul><li>New Hire</li><li>Employee Engagement</li></ul></div>
      <div class="box"><div class="box__head" style="background:var(--purple)">Employee Focused</div><ul><li>Summer Picnic</li><li>Employee Appreciation</li><li>Diwali</li><li>Holiday Party</li><li>Department Appreciation</li></ul></div>
      <div class="box" style="align-self:start"><div class="box__head" style="background:var(--purple)">Family Friendly</div><ul><li>Halloween</li><li>Bring your Kids to Work Day</li></ul></div>
    </div>
  </div>
  <div class="poster__footer">
    <div class="icon-set icon-set--collaboration" role="img" aria-label="Campaign icon set, collaboration icon leading"></div>
    <div class="brand"><span class="brand__mark"></span>Pelmaroq</div>
  </div>
</section>

</main>
</body>
</html>
```